TAMBERLY DISTRIBUTION VAN SIGNAGE

We would like a design done for our range of vans: the first van to be wrapped/logo'd will be a light grey corvane hauler if you wish to use this as template van. I have included our company logo( we do not need this redesigned) We like the design to be simple yet modern and funky. We need the Tamberly logo to be prominant. Other Details to include:

The phone number: +442847751932
Email: info@tamberly-example.eu.
Website: www.tamberly-example.eu

Target Market(s)

Retail stores

Font styles to use
Sans Serif

```html
<!DOCTYPE html>
<html lang="en">
<head>
<meta charset="utf-8">
<title>Tamberly Distribution – Van Signage</title>
<link rel="stylesheet" href="https://fonts.googleapis.com/css2?family=Josefin+Sans:wght@400;700&display=swap">
<style>
  :root {
    --bg: #ffffff;
    --panel-light: #f5f5f6;
    --panel-shade: #dadadc;
    --ink: #3a3a3c;
    --band: #3a3a3c;
    --band-soft: #d4d4d6;
    --on-band: #ffffff;
  }
  html, body {
    margin: 0;
    padding: 0;
    width: 1200px;
    height: 993px;
    overflow: hidden;
    background: var(--bg);
  }
  .canvas {
    display: block;
    width: 1200px;
    height: 993px;
    font-family: "Josefin Sans", sans-serif;
  }
  .wrap-panel { fill: url(#panelShade); }
  .accent-shape { fill: var(--band); }
  .info-band { fill: var(--band); }
  .status-band { fill: var(--band-soft); }
  .brand-mark { fill: none; stroke: var(--ink); stroke-width: 4; }
  .brand-name { fill: var(--ink); font-weight: 400; }
  .brand-name--main { font-size: 50px; letter-spacing: 3px; }
  .brand-name--sub { font-size: 34px; letter-spacing: 6px; }
  .phone { fill: var(--ink); font-size: 42px; font-weight: 700; }
  .contact-line { fill: var(--on-band); font-size: 21px; font-weight: 400; letter-spacing: 0.5px; }
  .status-line { fill: var(--ink); font-size: 22px; font-weight: 700; letter-spacing: 1px; }
</style>
</head>
<body>
<svg class="canvas" viewBox="0 0 1200 993" xmlns="http://www.w3.org/2000/svg">
  <defs>
    <linearGradient id="panelShade" x1="0" y1="0" x2="0" y2="1">
      <stop offset="0" stop-color="#f7f7f8"/>
      <stop offset="1" stop-color="#d8d8da"/>
    </linearGradient>
  </defs>

  <!-- Driver side (rear on left) -->
  <g class="van-side van-side--left">
    <rect class="wrap-panel" x="115" y="70" width="980" height="340" rx="30"/>
    <path class="accent-shape" d="M115 230 Q250 200 295 330 L300 410 L145 410 Q115 410 115 380 Z"/>
    <path class="accent-shape" d="M990 318 L1095 330 L1095 380 Q1095 410 1065 410 L990 410 Z"/>

    <circle class="brand-mark" cx="232" cy="160" r="38"/>
    <text class="brand-name brand-name--main" x="282" y="160">TAMBERLY</text>
    <text class="brand-name brand-name--sub" x="282" y="196">DISTRIBUTION</text>

    <text class="phone" x="378" y="284">+44-284-775-1932</text>
    <rect class="info-band" x="300" y="292" width="630" height="34"/>
    <text class="contact-line" x="615" y="318" text-anchor="middle">info@tamberly-example.eu  |  www.tamberly-example.eu</text>
    <rect class="status-band" x="300" y="330" width="560" height="30"/>
    <text class="status-line" x="580" y="354" text-anchor="middle">APPROVED CENTRAL BILLING STATUS</text>
  </g>

  <!-- Passenger side (rear on right) -->
  <g class="van-side van-side--right">
    <rect class="wrap-panel" x="105" y="510" width="980" height="340" rx="30"/>
    <path class="accent-shape" d="M1085 670 Q950 640 905 770 L900 850 L1055 850 Q1085 850 1085 820 Z"/>
    <path class="accent-shape" d="M210 758 L105 770 L105 820 Q105 850 135 850 L210 850 Z"/>

    <circle class="brand-mark" cx="640" cy="600" r="38"/>
    <text class="brand-name brand-name--main" x="690" y="600">TAMBERLY</text>
    <text class="brand-name brand-name--sub" x="690" y="636">DISTRIBUTION</text>

    <text class="phone" x="430" y="724">+44-284-775-1932</text>
    <rect class="info-band" x="310" y="732" width="630" height="34"/>
    <text class="contact-line" x="625" y="758" text-anchor="middle">info@tamberly-example.eu  |  www.tamberly-example.eu</text>
    <rect class="status-band" x="345" y="770" width="560" height="30"/>
    <text class="status-line" x="625" y="794" text-anchor="middle">APPROVED CENTRAL BILLING STATUS</text>
  </g>
</svg>
</body>
</html>
```